Investor Information Presentation Design Required and Corporate overview design

I have all the materials ready to go, just need 1x Pro Design for the presentation and 1x Pro Design for the corporate overview.
I am ok with images being changed (only if it represents the company better). Wording Can NOT be changed. Any process diagrams can be changed to better represent the process.
I can provide high res Logo file and obviously the files for the presentation and corporate overview. What I have done is basic, but need it to look far more polished and professional.

Target Market(s)

Fixed Term Deposits - $100,000 + High interest rates

Industry/Entity Type

Investment

Font styles to use
Sans Serif

Requirements
Must have
• A corporate professional look, think banks, financial services, business etc
• The presentation is NOT used for group presenting purposes - Individuals go through it on their own. Should want to make me feel like I have to read it all!

```html
<!DOCTYPE html>
<html lang="en">
<head>
<meta charset="utf-8">
<title>Norvale Capital – Corporate Overview</title>
<link rel="stylesheet" href="https://fonts.googleapis.com/css2?family=Montserrat:wght@400;500;600;700&family=Open+Sans:wght@400;600&display=swap">
<style>
:root{
  --canvas:#d8d9dc;
  --blue:#2a9fd8;
  --navy:#2e3a8c;
  --purple:#3d3990;
  --indigo:#4a4f9e;
  --slate:#8a8fa8;
  --ink:#2b2b33;
  --muted:#6d6f78;
  --rule:#2a9fd8;
}
*{box-sizing:border-box;margin:0;padding:0}
html,body{width:1048px;height:1200px;overflow:hidden;background:var(--canvas)}
body{font-family:"Open Sans",Arial,sans-serif;color:var(--ink)}
.deck{position:relative;width:1048px;height:1200px}
.slide{position:absolute;width:327px;height:184px;background:#fff;overflow:hidden;box-shadow:0 1px 3px rgba(0,0,0,.18)}
.c1{left:22px}.c2{left:360px}.c3{left:698px}
.r1{top:22px}.r2{top:216px}.r3{top:410px}.r4{top:604px}.r5{top:798px}.r6{top:992px}

.brand{font-family:"Montserrat",sans-serif;font-weight:600;font-size:9px;color:#fff;display:flex;align-items:center;gap:4px}
.brand i{display:block;width:14px;height:14px;border-radius:50%;background:currentColor}
.mini-brand{position:absolute;top:12px;right:12px;font-family:"Montserrat",sans-serif;font-weight:600;font-size:4.5px;color:var(--navy);text-align:center;line-height:1.2}
.mini-brand i{display:block;width:6px;height:6px;border-radius:50%;background:var(--navy);margin:0 auto 1px}

.title{font-family:"Montserrat",sans-serif;font-weight:600;font-size:10px;color:var(--ink);position:absolute;left:16px;top:14px}
.title b{color:var(--blue);font-weight:600}
.title::after{content:"";display:block;width:26px;height:1.2px;background:var(--ink);margin-top:2px}
.title.nobar::after{display:none}
.p{font-size:4.2px;line-height:1.45;color:var(--muted)}
.p em{color:var(--blue);font-style:italic}
.p .hl{color:var(--blue)}
.sub{font-family:"Montserrat",sans-serif;font-weight:600;font-size:4.6px;color:var(--ink);text-align:center}
.foot{position:absolute;left:16px;bottom:6px;font-size:3px;color:var(--muted)}
.foot span{color:var(--blue)}
.pg{position:absolute;right:12px;bottom:5px;width:9px;height:9px;border-radius:50%;background:var(--navy);color:#fff;font-size:3.6px;display:flex;align-items:center;justify-content:center}

.photo{position:absolute;left:0;top:0;width:100%}
.ph-office{background:linear-gradient(160deg,#6b7585,#2d3440 55%,#8a94a2)}
.ph-city{background:linear-gradient(170deg,#1b2947,#233a63 50%,#c79a4a 85%,#2a2f45)}
.ph-calc{background:linear-gradient(150deg,#9aa1a8,#545b63 60%,#2b3036)}
.ph-chart{background:linear-gradient(180deg,#0d1d36,#1a3f6c 55%,#c9a24c 80%,#3d4b5c)}
.ph-tablet{background:linear-gradient(140deg,#e2e6ea,#9fb2c4 45%,#47525e)}
.ph-card{background:linear-gradient(160deg,#6a6f77,#3a3e45 60%,#9a2b2f 90%)}
.ph-meeting{background:linear-gradient(150deg,#7e8793,#3d4450 60%,#5d6674)}
.photo .ovl{position:absolute;inset:0;display:flex;flex-direction:column;align-items:center;justify-content:center;color:#fff}
.ovl h2{font-family:"Montserrat",sans-serif;font-weight:500;font-size:11px}
.ovl p{font-size:4.3px;margin-top:4px}
.num{position:absolute;width:14px;height:14px;border-radius:50%;background:var(--blue);border:1.5px solid #fff;color:#fff;font-size:5px;font-family:"Montserrat",sans-serif;display:flex;align-items:center;justify-content:center;left:50%;transform:translateX(-50%)}
.inv h3{font-family:"Montserrat",sans-serif;font-weight:600;font-size:5px;color:var(--blue);margin-bottom:2px}
.inv h4{font-size:4.2px;font-weight:600;color:var(--ink);margin-top:3px}

.cover-top{position:absolute;left:0;top:0;width:100%;height:135px;background:linear-gradient(100deg,var(--blue),var(--navy) 85%)}
.cover-top.light{background:#fff}
.cover-head{position:absolute;left:16px;top:14px}
.cover-head h1{font-family:"Montserrat",sans-serif;font-weight:700;font-size:12px;margin-top:18px;color:#fff}
.cover-head .cc{font-size:6.5px;color:#fff;margin-top:2px}
.cover-head .co{font-size:4.5px;color:#fff;margin-top:8px;font-weight:600;line-height:1.3}
.cover-top.light .brand{color:var(--navy)}
.cover-top.light h1{color:var(--blue)}
.cover-top.light .cc,.cover-top.light .co{color:var(--ink)}
.cover-base{position:absolute;left:0;top:135px;width:100%;height:49px;padding:6px 16px}
.cover-base.band{background:var(--blue)}
.addr{display:flex;justify-content:space-between;font-size:3.4px;color:var(--muted);line-height:1.3}
.addr b{display:block;color:var(--blue);font-weight:600}
.band .addr,.band .disc{color:#fff}.band .addr b{color:#fff}
.disc{font-size:2.8px;color:var(--muted);line-height:1.35;margin-top:5px}

.obj{position:absolute;left:16px;right:16px;top:120px;display:grid;grid-template-columns:1fr 1fr;gap:6px 14px}
.obj div{display:flex;align-items:center;gap:5px;font-size:3.8px;color:var(--muted);line-height:1.35}
.obj b{flex:none;width:12px;height:9px;background:var(--blue);color:#fff;font-size:4px;display:flex;align-items:center;justify-content:center}

.kp{position:absolute;left:12px;right:12px;top:50px;height:108px;display:flex;gap:3px}
.kp div{flex:1;color:#fff;padding:16px 4px 4px;font-size:3.1px;line-height:1.35;position:relative}
.kp div::before{content:"";position:absolute;top:5px;left:50%;margin-left:-4px;width:8px;height:8px;border:.8px solid #fff;border-radius:50%}
.kp b{font-weight:600}

.sys{position:absolute;left:16px;right:16px;top:48px;height:112px;display:grid;grid-template-columns:repeat(5,1fr);grid-template-rows:1fr 1fr}
.sys div{display:flex;flex-direction:column;align-items:center;justify-content:center;padding:3px;font-size:3px;line-height:1.35;text-align:center;color:#fff}
.sys .g{background:#e4e6ec;color:var(--muted)}
.sys b{font-weight:600;display:block}

.region{display:flex;align-items:center;gap:4px;font-family:"Montserrat",sans-serif;font-weight:600;font-size:4.4px;color:var(--navy)}
.region i{width:13px;height:13px;border-radius:50%;background:var(--blue);flex:none}
.region::after{content:"";flex:1;height:.8px;background:var(--rule)}
.people{display:flex;gap:8px;margin-top:6px}
.person{display:flex;gap:3px;flex:1}
.person .face{width:12px;height:12px;border-radius:50%;background:#8d9099;flex:none}
.person .txt{font-size:2.6px;line-height:1.35;color:var(--muted)}
.person .txt b{display:block;color:var(--blue);font-weight:600;font-size:2.9px}

.qbullets{position:absolute;left:16px;right:16px;top:86px;display:grid;grid-template-columns:1fr 1fr;gap:0 12px}
.qbullets ul{list-style:disc;padding-left:5px}
.qbullets li{font-size:2.9px;line-height:1.35;color:var(--muted);margin-bottom:1.4px}

.fx{position:absolute;left:16px;right:16px;top:90px;display:flex;justify-content:space-between}
.fx h3{font-family:"Montserrat",sans-serif;font-weight:600;font-size:5px;color:var(--blue);margin-bottom:3px}
.fx p{font-size:4.1px;line-height:1.6;color:var(--ink)}

.contact{background:linear-gradient(100deg,var(--blue),var(--navy) 85%);color:#fff}
.contact .title{color:#fff}
.cgrid{position:absolute;left:16px;right:12px;top:46px;display:grid;grid-template-columns:repeat(3,1fr);gap:12px 8px}
.cgrid div{font-size:3px;line-height:1.4}
.cgrid b{display:block;font-size:4.5px;font-weight:600}
.cgrid small{display:block;font-size:3px;opacity:.85}
</style>
</head>
<body>
<main class="deck">

<section class="slide c1 r1">
  <div class="cover-top">
    <div class="cover-head">
      <div class="brand"><i></i>Norvale Capital</div>
      <h1>CORPORATE OVERVIEW</h1>
      <div class="cc">Commercial in Confidence</div>
      <div class="co">Norvale Capital Pty Ltd<br>ACN: 612 408 377</div>
    </div>
  </div>
  <div class="cover-base">
    <div class="addr">
      <div><b>Head Office</b>Level 8, 220 Harbour Street, Southbank<br>Victoria 3006</div>
      <div><b>Registered Office Address</b>Suite 4, 88 Queen Street, Melbourne<br>Victoria 3000</div>
      <div><b>Postal Address</b>PO Box 41876</div>
    </div>
    <p class="disc">Disclaimer – This document is not a prospectus under the Corporations Act and has not been lodged with ASIC. It does not contain all of the information that an investor would find in a prospectus. Recipients should seek independent advice before making any investment decision. The information is provided in good faith and is believed to be accurate at the time of writing.</p>
  </div>
</section>

<section class="slide c2 r1">
  <div class="cover-top light">
    <div class="cover-head">
      <div class="brand"><i></i>Norvale Capital</div>
      <h1>CORPORATE OVERVIEW</h1>
      <div class="cc">Commercial in Confidence</div>
      <div class="co">Norvale Capital Pty Ltd<br>ACN: 612 408 377</div>
    </div>
  </div>
  <div class="cover-base band">
    <div class="addr">
      <div><b>Head Office</b>Level 8, 220 Harbour Street, Southbank<br>Victoria 3006</div>
      <div><b>Registered Office Address</b>Suite 4, 88 Queen Street, Melbourne<br>Victoria 3000</div>
      <div><b>Postal Address</b>PO Box 41876</div>
    </div>
    <p class="disc">Disclaimer – This document is not a prospectus under the Corporations Act and has not been lodged with ASIC. It does not contain all of the information that an investor would find in a prospectus. Recipients should seek independent advice before making any investment decision. The information is provided in good faith and is believed to be accurate at the time of writing.</p>
  </div>
</section>

<section class="slide c3 r1">
  <h2 class="title nobar">Overview</h2>
  <div class="mini-brand"><i></i>Norvale Capital</div>
  <div style="position:absolute;left:16px;top:40px;width:86px;height:118px;border:.6px solid #cfd2d8;display:flex;align-items:center;justify-content:center">
    <div role="img" aria-label="Partner listing badge" style="width:50px;height:12px;background:var(--navy)"></div>
  </div>
  <div class="p" style="position:absolute;left:110px;right:16px;top:40px">
    <p>Norvale Capital is an <span class="hl">innovative investment</span> company that operates in a similar structure to a bank – it sources debt funding from private and corporate lenders to invest in pre-vetted investments that provide a rate of return higher than the cost of borrowing.</p>
    <p>Norvale Capital has access to <span class="hl">lucrative investment</span> opportunities due to its relationship with sister company Harbour Listing Group (HLG). HLG specialises in helping companies list on stock markets in Australia, and more recently London and New York, and its unique business model attracts investment opportunities not typically open to retail or wholesale investors.</p>
    <p>Norvale Capital currently works with <span class="hl">investors in 5 continents</span> (North America, United Kingdom, Australia, Asia and Africa) who have provided funding to Norvale Capital in return for a <span class="hl">fixed annual rate of return</span> that is <span class="hl">paid quarterly</span> to their nominated bank account. This simple investment structure provides investors with a simple yet effective means of earning a strong rate of return, which in many instances is a substantially higher return than they would otherwise achieve by placing money with a bank.</p>
  </div>
  <div class="foot">© 2016 by <span>Norvale Capital</span>. All rights reserved</div><div class="pg">2</div>
</section>

<section class="slide c1 r2">
  <div class="photo ph-office" style="height:92px" role="img" aria-label="Business people walking through a bright office lobby">
    <div class="ovl"><h2>Objectives</h2></div>
  </div>
  <p class="sub" style="position:absolute;left:0;right:0;top:100px">Norvale Capital has 4 key objectives -</p>
  <div class="obj">
    <div><b>01</b>Raise $150m from private and corporate lenders by December 2017</div>
    <div><b>03</b>Execute profitable investments on a consistent basis</div>
    <div><b>02</b>Provide a flawless service to its investors by always meeting financial commitments</div>
    <div><b>04</b>Invite its investor database to participate in other profitable investment opportunities</div>
  </div>
  <p class="p" style="position:absolute;left:16px;right:16px;top:158px;font-size:2.8px">Note: while Norvale Capital's objective is to raise funds, the rate of return is fixed and does not depend on investment performance of the business.</p>
  <div class="foot">© 2016 by <span>Norvale Capital</span>. All rights reserved</div><div class="pg">3</div>
</section>

<section class="slide c2 r2">
  <h2 class="title nobar"><b>Key Points</b> of Difference</h2>
  <div class="mini-brand"><i></i>Norvale Capital</div>
  <p class="sub" style="position:absolute;left:0;right:0;top:38px">The key components that make Norvale Capital stand out from other investment companies include -</p>
  <div class="kp">
    <div style="background:var(--blue)"><b>Global Presence</b> – Norvale Capital and HLG have a clear plan for scaling up operations in the UK, USA, Asia and Australian markets. Investors already see the strength of the group through the quarterly payments made to them.</div>
    <div style="background:var(--navy)"><b>Speed</b> – unlike traditional banks and smaller private investors, we operate efficiently, which enables Norvale Capital to secure more favourable investment terms due to the speed with which it can provide funding.</div>
    <div style="background:var(--purple)"><b>Innovation</b> – the evolution of Norvale Capital and HLG to what it is today is due to a constant drive for innovation based on listening to investor and client requirements, and also identifying major gaps within the financial services industry.</div>
    <div style="background:var(--slate)"><b>HLG</b> – operating a stock market listing service provides Norvale Capital with investment opportunities at discounts not typically available to retail and even wholesale investors, giving a return to investors on their capital invested.</div>
    <div style="background:var(--indigo)"><b>Network</b> – Norvale Capital and HLG have an extensive network spanning Australia, USA, Canada, United Kingdom and Asia. The network includes connections to brokers, fund managers and high net worth investors, which support the group's growth.</div>
  </div>
  <div class="foot">© 2016 by <span>Norvale Capital</span>. All rights reserved</div><div class="pg">4</div>
</section>

<section class="slide c3 r2">
  <div class="photo ph-city" style="width:165px;height:184px" role="img" aria-label="City skyline of office towers at night"></div>
  <h2 class="title nobar" style="left:172px"><b>Corporate</b> Structure</h2>
  <div class="p" style="position:absolute;left:172px;right:12px;top:40px;font-size:3.2px">
    <p>Norvale Capital is a private company registered with the Australian Securities and Investment Commission under company number 612 408 377. It is governed by the Corporations Act 2001 which governs the activities of private and public companies in Australia.</p>
    <p style="margin-top:3px;color:var(--ink);font-weight:600">Norvale Capital USA and UK</p>
    <p>In order to scale up Norvale Capital's international presence the company is currently seeking joint venture partners in the US and UK to open subsidiary companies to cater for their local market. The partners sought must have access to a substantial network of investors, are active in the investment space, can professionally represent Norvale Capital in their region and must be fully compliant with local securities regulations.</p>
    <p style="margin-top:3px;color:var(--ink);font-weight:600">Asset Holding Company</p>
    <p>Norvale Capital is in the process of finalising the set up of an entity that the Australian, US and UK companies will hold investment funds in to further strengthen the security of investments made on behalf of lenders.</p>
    <p>This asset holding company will be incorporated in a zero tax jurisdiction and hold the assets of Norvale Capital separate to the operating entities to provide an added layer of protection to investors.</p>
  </div>
  <div class="foot" style="left:172px">© 2016 by <span>Norvale Capital</span>. All rights reserved</div><div class="pg">5</div>
</section>

<section class="slide c1 r3">
  <h2 class="title">Raising Capital</h2>
  <div class="mini-brand"><i></i>Norvale Capital</div>
  <div class="p" style="position:absolute;left:16px;right:16px;top:40px;font-size:4.9px;color:var(--ink)">
    <p>Norvale Capital uses a highly effective digital marketing campaign for generating leads from potential investors. This campaign can be turned on/off at any time, and generates an average of $2m worth of investor interest every 24 hours when active.</p>
    <p style="margin-top:4px">Potential investors are qualified by in-house consultants who have been trained on Norvale Capital's business model such that they can explain the offering to investors and secure funding.</p>
    <p style="margin-top:4px">The company is finding a consistent flow of investment is being received through existing investors inviting others (e.g. family and friends) to be involved.</p>
    <p style="margin-top:4px">In addition to this, it is not uncommon for a large portion of investors to top up their investment after receiving their first quarterly interest payment (i.e. they see proof of concept and are comfortable in investing further money with Norvale Capital).</p>
  </div>
  <div class="foot">© 2016 by <span>Norvale Capital</span>. All rights reserved</div><div class="pg">6</div>
</section>

<section class="slide c2 r3">
  <div class="photo ph-calc" style="height:78px" role="img" aria-label="Calculator, pen and financial papers on a desk">
    <div class="ovl"><h2>Investments</h2><p>Norvale Capital is active in 4 categories of investment opportunities as follows -</p></div>
  </div>
  <div class="num" style="top:71px">01</div>
  <div class="p inv" style="position:absolute;left:16px;right:16px;top:92px;font-size:3.2px">
    <h3>1. Bridging Finance</h3>
    <p>Norvale Capital provides short term funding to companies that are about to undertake a major capital raise and need capital to cover costs such as legal, accounting and marketing before the raise is complete. This is typically offered to companies undertaking a listing with HLG.</p>
    <p>Norvale Capital typically charges 100% borrowing cost on these loans which have a 120 day average turnaround time and a maximum loan amount of $1m.</p>
    <p>Clients are prepared to pay this rate of return as the principal and interest is paid out of the larger amount of capital raised and means they can progress forward with their growth plans.</p>
    <h4>Example</h4>
    <p><em>Norvale Capital provided $600,000 to a mobile app client to cover listing process fees. The client repaid the loan plus the agreed fee within four months of the funds being advanced, returning a strong margin to Norvale Capital.</em></p>
  </div>
  <div class="foot">© 2016 by <span>Norvale Capital</span>. All rights reserved</div><div class="pg">7</div>
</section>

<section class="slide c3 r3">
  <div class="photo ph-chart" style="height:78px" role="img" aria-label="Stock market price chart on a trading screen"></div>
  <div class="num" style="top:71px">02</div>
  <div class="p inv" style="position:absolute;left:16px;right:16px;top:92px;font-size:3.2px">
    <h3>2. Pre-IPO Investments</h3>
    <p>Norvale Capital has access to lucrative pre-IPO investment opportunities due to its relationship with HLG. HLG provides a pipeline of companies with significant growth potential seeking capital ahead of listing, and Norvale Capital can invest in these at a substantial discount to the expected listing price.</p>
    <p>Substantial due diligence is done on such transactions prior to making the investment in order for the client to qualify for funding from Norvale Capital.</p>
    <h4>Example</h4>
    <p><em>HLG negotiated a 10% allocation for Norvale Capital in a fintech client ahead of its listing. The shares were acquired at a discount to the offer price and on listing traded well above the entry level, giving a strong return on the capital invested and a new avenue of opportunity for investors.</em></p>
  </div>
  <div class="foot">© 2016 by <span>Norvale Capital</span>. All rights reserved</div><div class="pg">8</div>
</section>

<section class="slide c1 r4">
  <div class="photo ph-tablet" style="height:78px" role="img" aria-label="Hand pointing a stylus at a tablet showing analytics"></div>
  <div class="num" style="top:71px">03</div>
  <div class="p inv" style="position:absolute;left:16px;right:16px;top:92px;font-size:3.2px">
    <h3>3. Short Term Working Capital</h3>
    <p>Norvale Capital provides short term working capital to clients that require funding to grow their businesses. This is typically done in return for either a high rate of interest (typically 50% p.a.) or equity shares in the company.</p>
    <h4>Example</h4>
    <p><em>A telecommunications client required an initial cash injection to kick-start their business which led to acquiring other companies. Norvale Capital provided a short term loan to facilitate growth in exchange for a shareholding and repayment of the loan at 100% borrowing cost within the next major capital raise.</em></p>
  </div>
  <div class="foot">© 2016 by <span>Norvale Capital</span>. All rights reserved</div><div class="pg">9</div>
</section>

<section class="slide c2 r4">
  <div class="photo ph-card" style="height:78px" role="img" aria-label="Hand holding a payment card near a laptop"></div>
  <div class="num" style="top:71px">04</div>
  <div class="p inv" style="position:absolute;left:16px;right:16px;top:92px;font-size:3.2px">
    <h3>4. Asset Purchases</h3>
    <p>Norvale Capital and HLG are often approached with fire-sale opportunities to purchase assets (listed and unlisted shares, property and other tangible assets) from vendors that urgently need to liquidate their holding. Where it can be verified, Norvale Capital may choose to purchase and on-sell or hold the asset in its portfolio.</p>
    <h4>Example</h4>
    <p><em>A broker approached Norvale Capital regarding a client who owned $1.2m worth of shares in a listed company and needed an urgent exit. The shares were acquired at a considerable discount and held until the market price recovered, at which point they were sold for a strong profit to the company.</em></p>
  </div>
  <div class="foot">© 2016 by <span>Norvale Capital</span>. All rights reserved</div><div class="pg">10</div>
</section>

<section class="slide c3 r4">
  <div class="photo ph-meeting" style="height:78px" role="img" aria-label="Business meeting around a table">
    <div class="ovl" style="justify-content:flex-start;padding-top:18px"><h2>Qualification of Investment Opportunities</h2></div>
  </div>
  <div style="position:absolute;left:0;right:0;top:60px;height:18px;background:var(--blue);color:#fff;font-size:3.4px;text-align:center;padding:4px 20px;line-height:1.35">Norvale Capital offers funding to less than 5% of all investment opportunities it is presented with, and when it does choose to provide funding, it does so on terms that are heavily in favour of Norvale Capital.</div>
  <p class="p" style="position:absolute;left:16px;top:81px;font-size:3.4px;color:var(--ink);font-weight:600">The due diligence procedures undertaken by Norvale Capital and HLG include -</p>
  <div class="qbullets">
    <ul>
      <li>Ensuring clients have clear written agreements prior to funding being released</li>
      <li>Face to face meetings with clients, typically conducted on site at the company's physical location</li>
      <li>Clients are reviewed against a 60+ point checklist to ensure suitability</li>
      <li>Review of key management team members and their track records</li>
      <li>Review of the financial position and forecasts of the business</li>
      <li>Market research into competition and industry trends</li>
    </ul>
    <ul>
      <li>Relevant company searches (e.g. official registry or local jurisdiction)</li>
      <li>Accountant and legal review of all contracts before signing</li>
      <li>Listed companies will heavily weigh on current share price and volume</li>
      <li>Due diligence procedures conducted by industry experts</li>
      <li>Security over assets where possible to protect the capital invested</li>
      <li>Regular monitoring of the client's progress after funding</li>
    </ul>
  </div>
  <p class="p" style="position:absolute;left:16px;right:16px;top:140px;font-size:3px">A large amount of opportunities brought to Norvale Capital and HLG that are not pursued are those that fall outside the strict criteria of due diligence. Norvale Capital and HLG only pursue opportunities where risk can be appropriately managed and the likelihood of a positive return on investment is high.</p>
  <div class="foot">© 2016 by <span>Norvale Capital</span>. All rights reserved</div><div class="pg">11</div>
</section>

<section class="slide c1 r5">
  <h2 class="title">Systems</h2>
  <div class="mini-brand"><i></i>Norvale Capital</div>
  <p class="sub" style="position:absolute;left:0;right:0;top:36px">Norvale Capital currently uses the following systems -</p>
  <div class="sys">
    <div class="g" role="img" aria-label="Binder folders icon">
      <svg width="34" height="26" viewBox="0 0 34 26"><rect x="2" y="2" width="8" height="22" fill="#2a9fd8"/><rect x="13" y="2" width="8" height="22" fill="#2a9fd8"/><rect x="24" y="2" width="8" height="22" fill="#2a9fd8"/><circle cx="6" cy="17" r="2" fill="#fff"/><circle cx="17" cy="17" r="2" fill="#fff"/><circle cx="28" cy="17" r="2" fill="#fff"/></svg>
    </div>
    <div style="background:var(--navy)"><b>CRM –</b>Relymark, a marketing automation system, has been heavily customised to provide Norvale Capital's consultants with a highly effective means of tracking interactions with new and existing clients.</div>
    <div class="g" role="img" aria-label="Cloud office suite icon">
      <svg width="28" height="22" viewBox="0 0 28 22"><rect x="2" y="2" width="24" height="18" rx="2" fill="none" stroke="#8a8fa8" stroke-width="1.5"/><rect x="6" y="6" width="6" height="4" fill="#2a9fd8"/><rect x="16" y="6" width="6" height="4" fill="#2e3a8c"/><rect x="6" y="12" width="6" height="4" fill="#8a8fa8"/><rect x="16" y="12" width="6" height="4" fill="#3d3990"/></svg>
    </div>
    <div style="background:var(--blue)"><b>Email –</b>All consultants use a Norvale Capital email address via Mailpoint, making remote and mobile access easy and cost effective.</div>
    <div class="g" role="img" aria-label="Client portal storefront icon">
      <svg width="26" height="24" viewBox="0 0 26 24"><path d="M2 8 L5 2 H21 L24 8 Z" fill="#3d3990"/><rect x="4" y="8" width="18" height="14" fill="none" stroke="#3d3990" stroke-width="1.5"/><rect x="10" y="13" width="6" height="9" fill="#3d3990"/></svg>
    </div>
    <div style="background:var(--blue)"><b>Bookkeeping –</b>Ledgerly is an award-winning cloud based accounting package used for the financial record keeping of Norvale Capital.</div>
    <div class="g" role="img" aria-label="CRM cycle icon">
      <svg width="26" height="26" viewBox="0 0 26 26"><circle cx="13" cy="13" r="10" fill="none" stroke="#2e3a8c" stroke-width="1.5" stroke-dasharray="12 4"/><circle cx="13" cy="13" r="5" fill="#2e3a8c"/></svg>
    </div>
    <div style="background:var(--navy)"><b>Cloudwork Suite –</b>A copy of all client loan agreements are stored in the cloud on Cloudwork Drive with a central record of all loans being maintained on Cloudwork Sheets.</div>
    <div class="g" role="img" aria-label="Email envelope icon">
      <svg width="26" height="20" viewBox="0 0 26 20"><rect x="2" y="2" width="22" height="16" fill="none" stroke="#2a9fd8" stroke-width="1.5"/><path d="M2 2 L13 11 L24 2" fill="none" stroke="#2a9fd8" stroke-width="1.5"/></svg>
    </div>
    <div style="background:var(--purple)"><b>Client Portal –</b>Norvale Capital is in the process of evaluating proposals for the implementation of an online client portal that will provide investors with access to their account information.</div>
  </div>
  <div class="foot">© 2016 by <span>Norvale Capital</span>. All rights reserved</div><div class="pg">12</div>
</section>

<section class="slide c2 r5">
  <h2 class="title nobar"><b>Our</b> Team</h2>
  <div class="mini-brand"><i></i>Norvale Capital</div>
  <p class="sub" style="position:absolute;left:0;right:0;top:36px">The following team members play an integral role in Norvale Capital's success -</p>
  <div style="position:absolute;left:12px;right:12px;top:46px">
    <div class="region"><i role="img" aria-label="Australia map"></i>AUSTRALIA</div>
    <div class="people" style="margin-top:10px">
      <div class="person"><div class="face" role="img" aria-label="Team member portrait"></div><div class="txt"><b>Daniel Okafor</b>Managing Director<br>Melbourne<br>Oversees strategy and growth</div></div>
      <div class="person"><div class="face" role="img" aria-label="Team member portrait"></div><div class="txt"><b>Ryan Holt</b>Head of Investments<br>Melbourne<br>Leads deal sourcing</div></div>
      <div class="person"><div class="face" role="img" aria-label="Team member portrait"></div><div class="txt"><b>Nadia Kerr</b>Business Development<br>Melbourne<br>Manages key investors</div></div>
      <div class="person"><div class="face" role="img" aria-label="Team member portrait"></div><div class="txt"><b>Helen Marsh</b>Compliance Manager<br>Melbourne<br>Oversees compliance</div></div>
      <div class="person"><div class="face" role="img" aria-label="Team member portrait"></div><div class="txt"><b>Ian Calder</b>Financial Controller<br>Melbourne<br>Handles reporting</div></div>
    </div>
    <div class="people" style="margin-top:12px">
      <div class="person"><div class="face" role="img" aria-label="Team member portrait"></div><div class="txt"><b>Kai Robertson</b>Investor Relations<br>Melbourne<br>Client onboarding</div></div>
      <div class="person"><div class="face" role="img" aria-label="Team member portrait"></div><div class="txt"><b>Ali Rahman</b>Senior Consultant<br>Melbourne<br>Investor enquiries</div></div>
      <div class="person"><div class="face" role="img" aria-label="Team member portrait"></div><div class="txt"><b>Tom Bailey</b>Senior Consultant<br>Melbourne<br>Investor enquiries</div></div>
      <div class="person"><div class="face" role="img" aria-label="Team member portrait"></div><div class="txt"><b>Jenna Price</b>Operations Manager<br>Melbourne<br>Runs daily operations</div></div>
      <div class="person"><div class="face" role="img" aria-label="Team member portrait"></div><div class="txt"><b>Sam Evans</b>Marketing Lead<br>Melbourne<br>Digital campaigns</div></div>
    </div>
  </div>
  <div class="foot">© 2016 by <span>Norvale Capital</span>. All rights reserved</div><div class="pg">13</div>
</section>

<section class="slide c3 r5">
  <div style="position:absolute;left:12px;right:12px;top:10px">
    <div class="region"><i role="img" aria-label="United Kingdom map"></i>UNITED KINGDOM</div>
    <div class="people" style="margin:10px 0 0 16px">
      <div class="person"><div class="face" role="img" aria-label="Team member portrait"></div><div class="txt"><b>Peter Lindqvist</b>Business Development Manager<br>London<br>Leads UK investor relations</div></div>
      <div class="person"><div class="face" role="img" aria-label="Team member portrait"></div><div class="txt"><b>Owen Blake</b>Senior Consultant<br>London<br>Supports UK investors</div></div>
      <div class="person"><div class="face" role="img" aria-label="Team member portrait"></div><div class="txt"><b>Marcus Reid</b>Independent Consultant<br>London<br>Advises on UK expansion</div></div>
    </div>
  </div>
  <div style="position:absolute;left:12px;right:12px;top:92px">
    <div class="region"><i role="img" aria-label="United States map"></i>USA</div>
    <div class="people" style="margin:10px 0 0 16px">
      <div class="person"><div class="face" role="img" aria-label="Team member portrait"></div><div class="txt"><b>Aaron Hayes</b>Managing Director, US<br>New York<br>Leads US operations</div></div>
      <div class="person"><div class="face" role="img" aria-label="Team member portrait"></div><div class="txt"><b>Erica Moss</b>Director of Operations<br>New York<br>Manages US investors</div></div>
      <div class="person"><div class="face" role="img" aria-label="Team member portrait"></div><div class="txt"><b>Nate Coleman</b>Vice President of Investor Relations<br>Florida</div></div>
    </div>
  </div>
  <div class="foot">© 2016 by <span>Norvale Capital</span>. All rights reserved</div><div class="pg">14</div>
</section>

<section class="slide c1 r6">
  <div style="position:absolute;left:12px;right:12px;top:8px">
    <div class="region"><i role="img" aria-label="Canada map"></i>CANADA</div>
    <div class="people" style="margin:6px 0 0 120px"><div class="person"><div class="face" role="img" aria-label="Team member portrait"></div><div class="txt"><b>Liam Fraser</b>Vice President of Investor Relations<br>Toronto, Canada</div></div></div>
  </div>
  <div style="position:absolute;left:12px;right:12px;top:62px">
    <div class="region"><i role="img" aria-label="Asia map"></i>ASIA</div>
    <div class="people" style="margin:6px 0 0 120px"><div class="person"><div class="face" role="img" aria-label="Team member portrait"></div><div class="txt"><b>Kevin Lau</b>Business Development Manager<br>Singapore<br>Leads Asian investor network</div></div></div>
  </div>
  <div style="position:absolute;left:12px;right:12px;top:116px">
    <div class="region"><i role="img" aria-label="World map"></i>GLOBAL</div>
    <div class="people" style="margin:6px 0 0 70px">
      <div class="person"><div class="face" role="img" aria-label="Team member portrait"></div><div class="txt"><b>Robert Kennard</b>Managing Director of HLG<br>Founder of the group<br>Guides global strategy</div></div>
      <div class="person"><div class="face" role="img" aria-label="Team member portrait"></div><div class="txt"><b>Claire Dubois</b>Personal Assistant to the MD<br>Coordinates global schedule</div></div>
    </div>
  </div>
  <div class="foot">© 2016 by <span>Norvale Capital</span>. All rights reserved</div><div class="pg">15</div>
</section>

<section class="slide c2 r6">
  <h2 class="title nobar">Foreign Exchange Partners</h2>
  <div class="mini-brand"><i></i>Norvale Capital</div>
  <p class="p" style="position:absolute;left:16px;right:16px;top:38px;font-size:4.8px;color:var(--ink)">Norvale Capital has relationships with two foreign exchange brokers who have assisted Norvale Capital lenders with converting their investment into Australian Dollars. Their services can save clients up to 5% on transaction fees as compared to normal banks, which can represent a potential saving of thousands of dollars. We suggest speaking with -</p>
  <div class="fx">
    <div>
      <h3>Meridian FX (Sydney)</h3>
      <p>Contact: Alan Porter<br>Email: <span style="color:var(--blue)">alan@meridianfx.example</span><br>Ph: +61 2 9000 1400<br>Web: www.meridianfx.example/norvale</p>
    </div>
    <div>
      <h3>Northstar Currency Inc (Ontario)</h3>
      <p>Contact: Sofia Renner<br>Email: sofia@northstarcurrency.example<br>Ph: 519-555-0130<br>Web: www.northstarcurrency.example</p>
    </div>
  </div>
  <div class="foot">© 2016 by <span>Norvale Capital</span>. All rights reserved</div><div class="pg">16</div>
</section>

<section class="slide c3 r6 contact">
  <h2 class="title nobar" style="top:16px">Contact Directory</h2>
  <div class="cgrid">
    <div>Making an Investment (AU or US)<b>Daniel Okafor</b><small>clientservices@norvalecapital.example<br>+61 420 555 811</small></div>
    <div>Making an Investment (UK or Europe)<b>Peter Lindqvist</b><small>clientservices.uk@norvalecapital.example<br>+44 77 5555 4290</small></div>
    <div>Finance Queries<b>Grace Tanudjaja</b><small>grace@harbourlisting.example<br>+61 430 555 946</small></div>
    <div>Customer Service Queries<b>Omar Siddiqui</b><small>manager@norvalecapital.example<br>+61 420 555 411</small></div>
    <div>Listing Enquiries (AU, US &amp; Asia)<b>Luca Ferreira</b><small>luca@harbourlisting.example<br>+61 432 555 465</small></div>
    <div>Listing Enquiries (Asia)<b>Kevin Lau</b><small>kevinlau@mail.example<br>+65 9555 2569</small></div>
    <div>Listing Enquiries (UK &amp; Europe)<b>Farid Noorani</b><small>farid@harbourlisting.example<br>+44 7555 418 952</small></div>
    <div>Seeking Investment<b>Claire Dubois</b><small>pa@harbourlisting.example<br>+61 475 555 864</small></div>
    <div>US &amp; UK Joint Venture Enquiries<b>Robert Kennard</b><small>robert@harbourlisting.example<br>+61 410 555 368</small></div>
  </div>
  <div class="brand" style="position:absolute;left:16px;bottom:8px;font-size:4px"><i style="width:6px;height:6px"></i>Norvale Capital</div>
  <div class="pg" style="background:#fff;color:var(--navy)">17</div>
</section>

</main>
</body>
</html>
```